Business Card Design Project

We need business cards for the new company Venture Loom based in Abu Dhabi, UAE, which provides IT retail solutions to businesses
Design should be done as a template, so we can add people when needed.
Please see attached details.
The brief is about 2 companies from our group. We need a business card only for Venture Loom
Industry/Entity Type
Retail
Look and feel
Each slider illustrates characteristics of the customer's brand and the style your logo design should communicate.

```html
<!DOCTYPE html>
<html lang="en">
<head>
<meta charset="utf-8">
<title>Venture Loom – Business Card</title>
<link href="https://fonts.googleapis.com/css2?family=Arimo:wght@400;700&family=Noto+Naskh+Arabic:wght@400&display=swap" rel="stylesheet">
<style>
  :root {
    --bg: #dcdcdc;
    --card: #ffffff;
    --purple: #4b3a94;
    --gold: #c9a417;
    --ink: #1d1d1d;
  }
  * { box-sizing: border-box; margin: 0; padding: 0; }
  html, body { width: 1200px; height: 840px; overflow: hidden; }
  body {
    background: var(--bg);
    font-family: "Arimo", Arial, sans-serif;
    position: relative;
  }
  .card {
    position: absolute;
    top: 275px;
    width: 464px;
    height: 266px;
    background: var(--card);
    overflow: hidden;
  }
  .card--front { left: 87px; }
  .card--back { left: 649px; }

  .brand {
    position: absolute;
    display: flex;
    align-items: center;
    gap: 8px;
    color: var(--purple);
    font-weight: 700;
    font-size: 26px;
    letter-spacing: -0.3px;
    white-space: nowrap;
  }
  .brand__mark {
    width: 14px; height: 14px;
    background: var(--gold);
    border-radius: 50%;
  }
  .card--front .brand { left: 50%; top: 50%; transform: translate(-50%, -50%); }
  .card--back .brand { left: 30px; top: 118px; font-size: 24px; }

  .contact {
    position: absolute;
    left: 241px;
    top: 45px;
    color: var(--ink);
  }
  .contact__name { color: var(--purple); font-size: 17px; font-weight: 400; line-height: 20px; }
  .contact__name-ar, .contact__role-ar {
    font-family: "Noto Naskh Arabic", serif;
    direction: rtl; text-align: left; unicode-bidi: plaintext;
    font-size: 12px; line-height: 16px;
  }
  .contact__name-ar { color: var(--purple); }
  .contact__role { color: var(--gold); font-size: 12.5px; line-height: 15px; }
  .contact__role-ar { color: var(--gold); }
  .contact__address { margin-top: 8px; font-size: 12.5px; line-height: 15px; }
  .contact__list { list-style: none; margin-top: 4px; }
  .contact__list li {
    display: flex; align-items: center; gap: 6px;
    font-size: 12.5px; line-height: 17px;
  }
  .contact__list svg { width: 12px; height: 12px; fill: var(--purple); flex: none; }

  .footer-band { position: absolute; left: 0; bottom: 0; width: 464px; height: 22px; }
  .footer-band__url {
    position: absolute; right: 77px; bottom: 4px;
    color: #fff; font-size: 12px; font-weight: 700;
  }
</style>
</head>
<body>

<section class="card card--front">
  <div class="brand"><span class="brand__mark"></span>Venture Loom</div>
</section>

<section class="card card--back">
  <div class="brand"><span class="brand__mark"></span>Venture Loom</div>

  <div class="contact">
    <p class="contact__name">Karim Haddad Nasser</p>
    <p class="contact__name-ar">كريم حداد</p>
    <p class="contact__role">Retail Solutions Manager</p>
    <p class="contact__role-ar">مدير حلول البيع بالتجزئة</p>
    <p class="contact__address">PO Box - 58210<br>Abu Dhabi, UAE</p>
    <ul class="contact__list">
      <li><svg viewBox="0 0 12 12"><path d="M2.5 1l2 2.2-1 1.2c.8 1.6 2 2.8 3.6 3.6l1.2-1L10.5 9l-1 1.8C5 10.5 1.5 7 1.2 2.5z"/></svg>02-5550182</li>
      <li><svg viewBox="0 0 12 12"><path d="M3.5 0.5h5v11h-5zM4.5 1.5v7h3v-7zM5.5 9.5h1v1h-1z" fill-rule="evenodd"/></svg>00971505550143</li>
      <li><svg viewBox="0 0 12 12"><path d="M3 1h6v3H3zM1 4.5h10v5H9V8H3v1.5H1zM3.5 8.5h5v3h-5z"/></svg>02-5550190</li>
      <li><svg viewBox="0 0 12 12"><path d="M1 2.5h10v7H1zM1.6 3l4.4 3.5L10.4 3"/></svg>karim.nasser@ventureloom.ae</li>
    </ul>
  </div>

  <svg class="footer-band" viewBox="0 0 464 22" aria-hidden="true">
    <polygon points="0,4 226,4 213,22 0,22" fill="var(--purple)"/>
    <polygon points="232,0 464,0 464,22 216,22" fill="var(--gold)"/>
  </svg>
  <span class="footer-band__url">www.ventureloom.ae</span>
</section>

</body>
</html>
```